Independent Movie Teaser Poster

I'm a director looking for a teaser poster (standard portrait poster dimensions-ratio of 27x40 in.) for an independent film, entitled Reeds The film is a road story (drama), so please feature a highway/car image (not a nice car-a beaten-up sedan along the lines of a 90's-era Venkor Astrelle), and preferably a southwestern-USA sunset motif. The colors should be bold and dramatic, leaning on reds and oranges. Example: http://www.plaverno.com/images/lf/panoKESTRIDGE.jpg

A good reference point would be the 'Ash Over Water' "Everything ends" ad campaign: http://cdn2.quilbyphoto.net/4471/4462842537_da8f4a7e21.jpg

Industry/Entity Type

Movie

Requirements
Must have
• Please feature the title Reeds in the largest font. then, in smaller font, the catchphrase Hold Fast. Go Slow. Live On. Let Go. And finally, in the smallest font, the words Coming Soon. The catchphrase and Coming Soon should be clustered together and separated from the title

Please use a conservative and elegant serif typeface
Nice to have
• None

```html
<!DOCTYPE html>
<html lang="en">
<head>
<meta charset="utf-8">
<title>Reeds — Teaser Poster</title>
<link rel="stylesheet" href="https://fonts.googleapis.com/css2?family=Playfair+Display:wght@700;900&family=Cormorant+Garamond:ital,wght@0,600;0,700;1,600&display=swap">
<style>
  :root {
    --sky-gold: #f6c76a;
    --sky-orange: #ef8a3a;
    --sky-red: #c8402a;
    --dusk-crimson: #7e1f1c;
    --asphalt: #3a1412;
    --asphalt-deep: #170807;
    --road-line: #ffc93a;
    --title-cream: #fff6e6;
    --accent-gold: #ffc93a;
  }
  html, body {
    margin: 0;
    padding: 0;
    width: 810px;
    height: 1200px;
    overflow: hidden;
    background: var(--asphalt-deep);
  }
  .poster {
    position: relative;
    width: 810px;
    height: 1200px;
    overflow: hidden;
  }
  .road-scene {
    position: absolute;
    inset: 0;
    background: linear-gradient(180deg,
      var(--sky-gold) 0%,
      var(--sky-orange) 14%,
      var(--sky-red) 26%,
      var(--dusk-crimson) 42%,
      var(--asphalt) 62%,
      #260c0b 80%,
      var(--asphalt-deep) 100%);
  }
  .artwork {
    position: absolute;
    inset: 0;
  }
  .centre-line { fill: var(--road-line); }
  .title {
    font-family: "Playfair Display", "Georgia", serif;
    font-weight: 900;
    font-size: 250px;
    fill: var(--title-cream);
  }
  .credits {
    position: absolute;
    right: 75px;
    top: 930px;
    width: 400px;
    text-align: right;
    color: var(--title-cream);
    line-height: 1;
  }
  .credits p { margin: 0; }
  .motto {
    font-family: "Playfair Display", "Georgia", serif;
    font-weight: 700;
    font-size: 34px;
    line-height: 1.2;
    letter-spacing: 0.5px;
    margin-bottom: 18px !important;
  }
  .kicker {
    font-family: "Cormorant Garamond", "Georgia", serif;
    font-style: italic;
    font-weight: 600;
    font-size: 20px;
    margin-bottom: 8px !important;
  }
  .release {
    font-family: "Cormorant Garamond", "Georgia", serif;
    font-weight: 700;
    font-size: 22px;
    letter-spacing: 4px;
    text-transform: uppercase;
  }
  .accent { color: var(--accent-gold); }
</style>
</head>
<body>
<main class="poster">
  <div class="road-scene" role="img" aria-label="Photograph of an empty southwestern desert highway running toward mesas under a red and orange sunset, with a beaten-up sedan on the road"></div>

  <svg class="artwork" width="810" height="1200" viewBox="0 0 810 1200" xmlns="http://www.w3.org/2000/svg">
    <g class="centre-line-band">
      <rect class="centre-line" x="240" y="0" width="62" height="58"/>
      <rect class="centre-line" x="240" y="79" width="62" height="233"/>
      <rect class="centre-line" x="240" y="333" width="62" height="234"/>
      <rect class="centre-line" x="240" y="588" width="62" height="228"/>
      <rect class="centre-line" x="240" y="837" width="62" height="230"/>
      <rect class="centre-line" x="240" y="1087" width="62" height="113"/>
    </g>
    <text class="title" x="75" y="800" textLength="660" lengthAdjust="spacingAndGlyphs">REEDS</text>
  </svg>

  <div class="credits">
    <p class="motto">Hold Fast. Go Slow.<br><span class="accent">Live On.</span> Let Go.</p>
    <p class="kicker">A story <span class="accent">from the road.</span></p>
    <p class="release"><span class="accent">Coming</span> Soon.</p>
  </div>
</main>
</body>
</html>
```